Harvest of Kingdoms
preparing the way of the Lord...
Modern
Tom Farrel
412 Co.Rd. 118 Marlow, Pa.17602
tomjane4Faith@postvale.com
www.tf-harvestofkingdoms.com
preaching the gospel of Jesus, and teaching others to do the same.
mission trips
rallies and revivals
camps
this is for business cards and letterhead...

```html
<!DOCTYPE html>
<html lang="en">
<head>
<meta charset="utf-8">
<title>Harvest of Kingdoms – Business Card Set</title>
<link href="https://fonts.googleapis.com/css2?family=Cinzel:wght@400&family=Tinos:wght@400&display=swap" rel="stylesheet">
<style>
  :root {
    --sheet: #ececec;
    --sheet-edge: #9a9a9a;
    --paper: #ffffff;
    --ink: #1f2a33;
    --name-green: #2e8f3e;
    --green-light: #4cc15a;
    --green-dark: #2a9a3a;
    --field-green-center: #3aa35a;
    --field-green-edge: #0b6a2c;
    --field-blue-center: #86a9d6;
    --field-blue-edge: #3f6fae;
    --wave-line: #111111;
    --contact: #ffffff;
  }
  * { margin: 0; padding: 0; box-sizing: border-box; }
  html, body { width: 1200px; height: 722px; overflow: hidden; background: var(--sheet); }
  .sheet {
    position: relative; width: 1200px; height: 722px;
    background: var(--sheet); border: 2px solid var(--sheet-edge);
  }
  .card {
    position: absolute; width: 570px; height: 334px; overflow: hidden;
    border: 1px solid #c8c8c8;
  }
  .card--front { left: 19px; top: 19px; background: var(--paper); }
  .card--green { left: 608px; top: 19px;
    background: radial-gradient(ellipse at 55% 45%, var(--field-green-center) 0%, #1f8a42 45%, var(--field-green-edge) 100%); }
  .card--white { left: 19px; top: 372px; background: var(--paper); }
  .card--blue { left: 608px; top: 372px;
    background: radial-gradient(ellipse at 50% 30%, var(--field-blue-center) 0%, #6d93c8 50%, var(--field-blue-edge) 100%); }

  .wordmark {
    display: flex; align-items: center; gap: 10px;
    font-family: "Cinzel", serif; font-weight: 400; color: var(--ink);
    white-space: nowrap; letter-spacing: 0.5px;
  }
  .wordmark__dot { width: 0.8em; height: 0.8em; border-radius: 50%; background: var(--ink); flex: none; }
  .card--front .wordmark { position: absolute; left: 18px; top: 38px; font-size: 30px; }
  .wordmark--center { position: absolute; left: 0; right: 0; top: 0; bottom: 0; justify-content: center; font-size: 40px; }

  .front__wave { position: absolute; left: 0; top: 0; width: 570px; height: 334px; }
  .front__person { position: absolute; left: 230px; top: 160px; text-align: center; font-family: "Tinos", serif; }
  .front__name { color: var(--name-green); font-size: 21px; line-height: 1.2; }
  .front__org { color: #111; font-size: 14px; line-height: 1.4; }
  .front__contact {
    position: absolute; left: 22px; top: 245px;
    font-family: "Tinos", serif; font-size: 14px; line-height: 17px; color: var(--contact);
    list-style: none;
  }
</style>
</head>
<body>
<main class="sheet">
  <section class="card card--front">
    <svg class="front__wave" viewBox="0 0 570 334" aria-hidden="true">
      <defs>
        <linearGradient id="frontGreen" x1="0" y1="0" x2="0" y2="1">
          <stop offset="0" stop-color="var(--green-light)"/>
          <stop offset="1" stop-color="var(--green-dark)"/>
        </linearGradient>
      </defs>
      <path d="M0,168 C90,225 260,250 400,232 C470,223 530,212 570,206 L570,334 L0,334 Z" fill="url(#frontGreen)"/>
      <path d="M0,168 C90,225 260,250 400,232 C470,223 530,212 570,206" fill="none" stroke="var(--wave-line)" stroke-width="3"/>
    </svg>
    <div class="wordmark"><span class="wordmark__dot"></span>Harvest of Kingdoms</div>
    <div class="front__person">
      <p class="front__name">Tom Farrel</p>
      <p class="front__org">Harvest of Kingdoms</p>
    </div>
    <ul class="front__contact">
      <li>412 Co.Rd. 118 Marlow, Pa.17602</li>
      <li>Toll free: 570.555.0142</li>
      <li>Email: tomjane4Faith@postvale.com</li>
      <li>www.tf-harvestofkingdoms.com</li>
    </ul>
  </section>

  <section class="card card--green">
    <div class="wordmark wordmark--center"><span class="wordmark__dot"></span>Harvest of Kingdoms</div>
  </section>

  <section class="card card--white">
    <div class="wordmark wordmark--center"><span class="wordmark__dot"></span>Harvest of Kingdoms</div>
  </section>

  <section class="card card--blue">
    <div class="wordmark wordmark--center"><span class="wordmark__dot"></span>Harvest of Kingdoms</div>
  </section>
</main>
</body>
</html>
```